Brivora Australia Company Values.

We have just completed our company purpose, beliefs and values (for the first time, we have not had these before)
We are now wanting to add images to each company value as a visual
so they are easily identified and understood for all our staff - we need them to remember the 5 Values.
We are a manufacturer of dental materials and infection control products, based in Melbourne.

What we would like:
- A Poster (that can be placed in our staff lunch rooms)
- The values to be lined up Horizontally
- Image on the top of the words
- Wording does not all need to be the same text font
- No image photographs - please use image graphics
- No images with people
- No dental related graphics

Target audience: Brivora staff

Our Values are:
Think Big
Have a go, learn and adapt
If you're gonna do it, do it bloody well
Empower Others
Be a good human

I have uploaded some examples.

Target Market(s)

Brivora Team members

Industry/Entity Type

Healthcare

Colors

Designer to choose colors to be used in the design.

Requirements
Must have
• Clear horizontal layout, space between each value
Should not have
• No images with humans or dental

```html
<!DOCTYPE html>
<html lang="en">
<head>
<meta charset="utf-8">
<title>Brivora Australia – Company Values</title>
<link rel="stylesheet" href="https://fonts.googleapis.com/css2?family=Fredoka:wght@600&family=Lilita+One&family=Wellfleet&display=swap">
<style>
  :root {
    --band-blue: #2784fb;
    --stripe-gold: #f9ae0d;
    --ring-gold: #f2aa17;
    --text-gold: #f6ac1b;
    --paper: #ffffff;
  }
  * { margin: 0; padding: 0; box-sizing: border-box; }
  html, body { width: 1200px; height: 807px; overflow: hidden; background: var(--paper); }
  .poster { position: relative; width: 1200px; height: 807px; background: var(--paper); }
  .band { position: absolute; left: 0; width: 1200px; background: var(--band-blue); }
  .band--top { top: 0; height: 151px; }
  .band--bottom { top: 681px; height: 126px; }
  .stripe { position: absolute; left: 0; width: 1200px; background: var(--stripe-gold); }
  .stripe--top { top: 151px; height: 22px; }
  .stripe--bottom { top: 661px; height: 20px; }

  .value-icons { position: absolute; left: 0; top: 0; }

  .value-card {
    position: absolute; top: 417px; width: 194px; height: 188px;
    border: 5px solid var(--ring-gold); border-radius: 36px;
    display: flex; align-items: center; justify-content: center;
    text-align: center; color: var(--text-gold);
  }
  .value-card--think { left: 29px; }
  .value-card--go { left: 262px; }
  .value-card--well { left: 508px; }
  .value-card--empower { left: 747px; }
  .value-card--human { left: 983px; }

  .value-name--rounded {
    font-family: "Fredoka", "Lilita One", sans-serif; font-weight: 600;
    font-size: 30px; line-height: 1.25; letter-spacing: 0.3px;
  }
  .value-card--go .value-name--rounded { font-size: 29px; }
  .value-name--italic {
    font-family: "Lilita One", sans-serif; font-size: 23px; line-height: 1.4;
    transform: skewX(-12deg); text-align: left; letter-spacing: 0.5px;
  }
  .value-name--italic span { display: block; }
  .value-name--italic span:nth-child(2) { padding-left: 2px; }
  .value-name--italic span:nth-child(3) { padding-left: 38px; }
  .value-name--serif {
    font-family: "Wellfleet", serif; font-size: 33px; line-height: 1.3;
    color: var(--text-gold); -webkit-text-stroke: 0.6px #e79b0a;
  }
  .value-name--block {
    font-family: "Lilita One", sans-serif; font-size: 32px; line-height: 1.15; letter-spacing: 0.5px;
  }
</style>
</head>
<body>
<main class="poster">
  <div class="band band--top"></div>
  <div class="stripe stripe--top"></div>

  <svg class="value-icons" width="1200" height="807" viewBox="0 0 1200 807">
    <defs>
      <radialGradient id="bulb-fill" cx="50%" cy="45%" r="55%">
        <stop offset="0" stop-color="#f7a531"/><stop offset="1" stop-color="#fde7c6"/>
      </radialGradient>
      <radialGradient id="plane-fill" cx="50%" cy="50%" r="55%">
        <stop offset="0" stop-color="#9fe6c0"/><stop offset="1" stop-color="#fde8bf"/>
      </radialGradient>
      <radialGradient id="search-fill" cx="50%" cy="50%" r="55%">
        <stop offset="0" stop-color="#c9d1e8"/><stop offset="1" stop-color="#f3f5fb"/>
      </radialGradient>
      <radialGradient id="circle-fill" cx="50%" cy="50%" r="55%">
        <stop offset="0" stop-color="#f7b6d8"/><stop offset="1" stop-color="#c9ecd2"/>
      </radialGradient>
      <radialGradient id="seedling-fill" cx="50%" cy="50%" r="55%">
        <stop offset="0" stop-color="#a6d96a"/><stop offset="1" stop-color="#f2dcc6"/>
      </radialGradient>
    </defs>
    <g fill="none" stroke="var(--ring-gold)" stroke-width="6">
      <circle cx="135" cy="305" r="86"/>
      <circle cx="361" cy="305" r="86"/>
      <circle cx="600" cy="305" r="86"/>
      <circle cx="848" cy="305" r="86"/>
      <circle cx="1084" cy="305" r="86"/>
    </g>
    <circle cx="135" cy="305" r="72" fill="url(#bulb-fill)" role="img" aria-label="Light bulb with a brain inside, giving off rays"/>
    <circle cx="361" cy="305" r="72" fill="url(#plane-fill)" role="img" aria-label="Green and orange paper plane"/>
    <circle cx="600" cy="305" r="72" fill="url(#search-fill)" role="img" aria-label="Magnifying glass held up close"/>
    <circle cx="848" cy="305" r="72" fill="url(#circle-fill)" role="img" aria-label="Ring of colourful joined hands"/>
    <circle cx="1084" cy="305" r="72" fill="url(#seedling-fill)" role="img" aria-label="Young green seedling in a handful of soil"/>
  </svg>

  <div class="value-card value-card--think"><p class="value-name--rounded">THINK BIG</p></div>
  <div class="value-card value-card--go"><p class="value-name--rounded">HAVE A GO,<br>LEARN &amp;<br>ADAPT</p></div>
  <div class="value-card value-card--well">
    <p class="value-name--italic"><span>IF YOU'RE</span><span>GONNA DO IT,</span><span>DO IT</span><span>BLOODY WELL</span></p>
  </div>
  <div class="value-card value-card--empower"><p class="value-name--serif">EMPOWER<br>OTHERS</p></div>
  <div class="value-card value-card--human"><p class="value-name--block">BE A GOOD<br>HUMAN</p></div>

  <div class="stripe stripe--bottom"></div>
  <div class="band band--bottom"></div>
</main>
</body>
</html>
```